7 D Thinking

Re: Personal development plan based on reflection & introspection

To do

• One pager as shown in the uploaded files ( the blue version )
• Small Power Point with 7 or 8 slides

Title :

Disruptive people have 7 D Thinking Mindsets

1) Dissatisfied
----------------
2) Dream
3) Desire
4) Determination
5) Discipline
6) Drive
----------------
7) Disrupt

To be used for
• For a One on one discussion
• A personal Digital Intake call via my website
• Power Point presentation 7or 8 slides

Basis for the one pager and PPT

 
Please find herewith 2 documents related to 5-Dimensional Thinking
 
I use this canvas to question myself or help friends.
 
Getting older and wiser I added a 6th and 7th dimension: Dissatisfaction & Disruption.

Sources about me
https://www.maxorlanfield.lu/
https://www.maxorlanfield.lu/who-i-am-2/
http://pooledideasforum.com/about/
https://www.profilenet.com/in/morlanfield/?ppe=1

Topics to bring on the one pager & PPT

 
1. Dissatisfied 

2. Dream
3.  Desire
4. Determination
5. Discipline
6.  Drive

7. Disrupted

Style & Colors

• My favorite color is Blue
• My disruptive color is RED

Disruption :meaning
specialized business to change the traditional way that an industry operates, especially in a new and effective way:
Korvane Inc. disrupted the traditional way of selling computers by switching to the internet.
Examples from the crowdsourced world Zivo, Nestora etc..

 
How do you start your introspection?
 
A  Write down on a paper how Dissatisfied you are with your actual situation.
 
B  Go to the loop and start with defining your Dream and follow the method.
 
C  Find out how you can be a Disruptor for yourself or others
Updates

Reason: Ok,it is the first time I use SketchHive. I did set up a poll Did not receive meaningfull feed back so far I will decide in 5 days so please extend Maxime

Target Market(s)

People who are dissatisfied with their life either from PRIVATE either from PROFESSIONAL point of view
High level educated people, business related , being able to make up their -personal change plan.

Industry/Entity Type

Business Consultant

Font styles to use
Other font styles liked:
• Helvetica, Arial

Colors
ec1f27
0355a3
ffffff

Requirements
Must have
• 2 circles / loops
• A loop starting with
• 1 -Dissatisfied ( I am not happy with my life personal /business- I want change )
• ending with
• 7 Disrupt
• All words by topic (1 to 7 ) you find on the uploaded files
• A inner loop with the 5 initial D,s
Nice to have
• a movement , 2 cirlces
• business style
• I am a consultant
• Wanting to help people creating a better world by giving them a tool for reflection to re-invent themselves
Should not have
• gender related words

```html
<!DOCTYPE html>
<html lang="en">
<head>
<meta charset="utf-8">
<title>7D Thinking</title>
<link rel="stylesheet" href="https://fonts.googleapis.com/css2?family=Anton&display=swap">
<style>
  :root {
    --bg-blue: #1558a0;
    --ring-blue: #3d9fd6;
    --sky: #4fa2cf;
    --sky-edge: #3a86bf;
    --lime: #d7e71f;
    --lime-edge: #a9bb2a;
    --orange: #f9a122;
    --orange-edge: #e4861b;
    --red: #ec1f27;
    --red-edge: #8a1218;
    --white: #ffffff;
    --ink: #111111;
  }
  html, body {
    margin: 0;
    padding: 0;
    width: 1200px;
    height: 849px;
    overflow: hidden;
    background: var(--bg-blue);
  }
  .canvas {
    display: block;
    width: 1200px;
    height: 849px;
  }
  .ring {
    fill: none;
    stroke: var(--ring-blue);
    stroke-width: 1.6;
  }
  .label {
    font-family: "Anton", "Arial Narrow", sans-serif;
    text-anchor: middle;
    dominant-baseline: central;
    fill: var(--ink);
  }
  .label--light { fill: var(--white); }
  .node--sky { fill: var(--sky); stroke: var(--sky-edge); stroke-width: 2; }
  .node--lime { fill: var(--lime); stroke: var(--lime-edge); stroke-width: 2; }
  .node--orange { fill: var(--orange); stroke: var(--orange-edge); stroke-width: 2; }
  .node--red { fill: var(--red); stroke: var(--red-edge); stroke-width: 3; }
  .hub { fill: var(--white); }
</style>
</head>
<body>
<svg class="canvas" viewBox="0 0 1200 849" xmlns="http://www.w3.org/2000/svg" role="img" aria-label="7D Thinking: outer loop from Dissatisfied to Disrupted, inner loop Dream, Desire, Determination, Discipline, Drive">
  <rect width="1200" height="849" fill="var(--bg-blue)"/>

  <circle class="ring ring--outer" cx="573" cy="409" r="339"/>
  <circle class="ring ring--inner" cx="597" cy="405" r="214"/>

  <g class="hub-group">
    <circle class="hub" cx="621" cy="402" r="103"/>
    <text class="label hub-title" x="621" y="375" font-size="70">7D</text>
    <text class="label hub-subtitle" x="621" y="430" font-size="40">Thinking</text>
  </g>

  <g class="step step--dissatisfied">
    <circle class="node--sky" cx="628" cy="97" r="60"/>
    <text class="label label--light" x="628" y="97" font-size="18">Dissatisfied</text>
  </g>

  <g class="step step--desire">
    <circle class="node--orange" cx="497" cy="211" r="48"/>
    <text class="label" x="497" y="211" font-size="23">Desire</text>
  </g>

  <g class="step step--dream">
    <circle class="node--lime" cx="745" cy="248" r="48"/>
    <text class="label" x="745" y="248" font-size="21">Dream</text>
  </g>

  <g class="step step--determination">
    <circle class="node--lime" cx="361" cy="378" r="90"/>
    <text class="label" x="365" y="377" font-size="24">Determination</text>
  </g>

  <g class="step step--discipline">
    <circle class="node--orange" cx="485" cy="584" r="71"/>
    <text class="label" x="489" y="584" font-size="26">Discipline</text>
  </g>

  <g class="step step--drive">
    <circle class="node--orange" cx="777" cy="532" r="47"/>
    <text class="label" x="777" y="532" font-size="24">Drive</text>
  </g>

  <g class="step step--disrupted">
    <circle class="node--red" cx="641" cy="730" r="58"/>
    <text class="label label--light" x="641" y="730" font-size="19">Disrupted</text>
  </g>
</svg>
</body>
</html>
```